Flyer für einen Sanitär Heizungs Betrieb
Zielgruppe
Sanitär Heizungs Betrieb der den Fokus verstärkt auf den Service an Heizungsanlagen setzten will.
Der Flyer soll sowohl an Privathaushalte als auch an Hausverwaltungen gehen.
Er soll unsere Leistungen aufzeigen und einen guten ersten Eindruck vermitteln.
Aufgabenstellung
Anbei sende ich Themen die als Leistung aufgeführt werden, sowie Strichwort für einen Werbetext (kann gerne generiert werden ansonsten kommt er noch zum texter)

```html
<!DOCTYPE html>
<html lang="de">
<head>
<meta charset="UTF-8">
<title>Unsere Leistungen für Sie</title>
<link rel="stylesheet" href="https://fonts.googleapis.com/css2?family=Open+Sans:wght@400;700&display=swap">
<style>
  :root {
    --brand-blue: #1a77c2;
    --title-ink: #2b2b2b;
    --paper: #ffffff;
    --text-light: #ffffff;
  }
  * { box-sizing: border-box; margin: 0; padding: 0; }
  html, body { width: 853px; height: 1200px; overflow: hidden; background: var(--paper); }
  body { font-family: "Open Sans", Arial, sans-serif; }
  .flyer { width: 853px; height: 1200px; display: flex; flex-direction: column; }
  .flyer-title {
    height: 84px;
    display: flex; align-items: center; justify-content: center;
    font-size: 37px; font-weight: 700; letter-spacing: 0.5px;
    color: var(--title-ink);
  }
  .service-row { display: flex; height: 279px; }
  .service-text {
    width: 425px;
    background: var(--brand-blue);
    color: var(--text-light);
    display: flex; flex-direction: column; justify-content: center;
    padding: 0 30px;
  }
  .service-row.reverse .service-text { width: 428px; padding: 0 30px 0 28px; }
  .service-media { flex: 1; }
  .service-item + .service-item { margin-top: 22px; }
  .service-item h2 {
    font-size: 17.5px; font-weight: 700; line-height: 1.3; text-transform: uppercase;
  }
  .service-item p { font-size: 17px; font-weight: 400; line-height: 1.4; }
  .media-technician {
    background: linear-gradient(135deg, #eef0f1 0%, #dcdfe2 40%, #3d5f9a 62%, #f2f2f0 85%, #ffffff 100%);
  }
  .media-solar {
    background: linear-gradient(160deg, #7fa4d6 0%, #3e6fb8 35%, #274f94 65%, #1c3a70 100%);
  }
  .media-boiler {
    background: linear-gradient(120deg, #f1f1f1 0%, #d9d7d4 35%, #4a607f 55%, #eeeeee 75%, #ffffff 100%);
  }
  .media-plantroom {
    background: linear-gradient(180deg, #f4f5f6 0%, #d3d7db 45%, #b9bec4 75%, #8e959c 100%);
  }
</style>
</head>
<body>
<main class="flyer">
  <h1 class="flyer-title">UNSERE LEISTUNGEN FÜR SIE</h1>

  <section class="service-row">
    <div class="service-text">
      <div class="service-item">
        <h2>Notdienst Heizung:</h2>
        <p>Soforthilfe im Notfall für Heizungs&shy;probleme</p>
      </div>
      <div class="service-item">
        <h2>Wartung:</h2>
        <p>Allgemeine Heizungsdienstleistungen für Öl, Gas, Solaranlagen, Wärmepum&shy;pen und Gasgeräte</p>
      </div>
    </div>
    <div class="service-media media-technician" role="img" aria-label="Foto: Heizungsmonteur mit gelbem Helm arbeitet an Rohrleitungen"></div>
  </section>

  <section class="service-row reverse">
    <div class="service-media media-solar" role="img" aria-label="Foto: Reihen von Solarmodulen"></div>
    <div class="service-text">
      <div class="service-item">
        <h2>Solaranlagenservice:</h2>
        <p>Spülen und Entlüften von Solaranlagen</p>
      </div>
      <div class="service-item">
        <h2>Flexible Hilfe:</h2>
        <p>Schnelle, unkomplizierte Unterstützung bei verschiedenen Anliegen</p>
      </div>
    </div>
  </section>

  <section class="service-row">
    <div class="service-text">
      <div class="service-item">
        <h2>Törungsbeseitigung:</h2>
        <p>Reparaturen und Problemlösungen für Heizungs- und Sanitäranlagen</p>
      </div>
      <div class="service-item">
        <h2>Austausch &amp; Modernisierung:</h2>
        <p>Erneuerung und zeitgemäße Moderni&shy;sierung von Heizungsanlagen</p>
      </div>
    </div>
    <div class="service-media media-boiler" role="img" aria-label="Foto: Techniker stellt eine wandhängende Gastherme ein"></div>
  </section>

  <section class="service-row reverse">
    <div class="service-media media-plantroom" role="img" aria-label="Foto: moderner Heizungsraum mit Rohrleitungen und Kesseln"></div>
    <div class="service-text">
      <div class="service-item">
        <h2>Wasserqualitätstest:</h2>
        <p>Prüfung und Aufbereitung des Heizungs&shy;wassers nach VDI 123 Standard</p>
      </div>
      <div class="service-item">
        <h2>Heizungsanlagenspülung:</h2>
        <p>Reinigung von Fußbodenheizungen durch Spülen der Heizungsanlagen</p>
      </div>
    </div>
  </section>
</main>
</body>
</html>
```